Advertising company unique advertising platform

we need a logo design for a new company based in Australia Melbourne. We develop innovated advertising platform where consumer can use this platform to get regular discount, as business owner they can use this platform for free advertisement. Payment for this advertisement platform only payable every two weeks, when I generate revenue for their business

Industry/Entity Type

Advertising

Contact Information for Business Card

Dale Pruitt | Co-Founder |Managing Director
Suite 718 263 Harrowgate Row Melbourne Vic 3000

ABN 41 902 615 273
Tel: +61 0491 528 307 | Email: dale.pruitt@corvelaxtro.com

Font styles to use
Decorative
Script

Requirements
Must have
• Try few different design and some round corner business card
Should not have
• One round corner business card...try 4 different colour background not only black, make sure two side is designed. Be creative so imagine you are giving this to a client make sure has wow factor, if you can also try one design with engrave like all the logo, words look 3d feel
• The word Advertising Platform use attached file font

```html
<!DOCTYPE html>
<html lang="en">
<head>
<meta charset="UTF-8">
<title>Relaymark Hub – Business Card</title>
<link href="https://fonts.googleapis.com/css2?family=Montserrat:wght@400;500;600&display=swap" rel="stylesheet">
<style>
  :root {
    --backdrop: #e6f5ef;
    --card-dark: #2a2a2a;
    --sun: #fcdc58;
    --leaf: #6fc79b;
    --sky: #7fa0d2;
    --rose: #c97a6e;
    --flame: #f07a2c;
    --name-yellow: #f4d33a;
    --text-light: #f2f2f2;
    --rule-gold: #a88b3a;
  }
  * { box-sizing: border-box; margin: 0; padding: 0; }
  html, body {
    width: 1200px; height: 1200px; overflow: hidden;
    background: var(--backdrop);
    font-family: "Montserrat", sans-serif;
  }
  .sheet {
    width: 1200px; height: 1200px;
    display: flex; flex-direction: column; align-items: center; justify-content: center;
    gap: 60px;
  }
  .card {
    position: relative;
    width: 820px; height: 470px;
    border-radius: 44px;
    overflow: hidden;
    box-shadow: 0 14px 30px rgba(0,0,0,0.18);
  }
  .card-front {
    background: linear-gradient(100deg, #c9d77a 0%, var(--sun) 18%, #bcd37f 36%, var(--leaf) 50%, #7bb2bd 64%, var(--sky) 80%, var(--rose) 100%);
    display: flex; align-items: center; justify-content: center;
  }
  .brand { display: flex; align-items: center; gap: 18px; }
  .brand-dot { border-radius: 50%; background: var(--flame); flex: none; }
  .brand-name { font-weight: 600; color: var(--flame); white-space: nowrap; }
  .card-front .brand-dot { width: 70px; height: 70px; }
  .card-front .brand-name { font-size: 54px; }

  .card-back { background: var(--card-dark); color: var(--text-light); }
  .corner-glow { position: absolute; top: 0; right: 0; }
  .back-brand { position: absolute; left: 60px; top: 58px; }
  .back-brand .brand { gap: 14px; }
  .back-brand .brand-dot { width: 48px; height: 48px; }
  .back-brand .brand-name { font-size: 32px; }
  .abn { margin: 8px 0 0 62px; font-size: 15px; letter-spacing: 0.3px; }
  .contact { position: absolute; left: 60px; top: 228px; right: 60px; }
  .person-name { font-size: 42px; font-weight: 500; color: var(--name-yellow); }
  .person-role { font-size: 20px; margin-top: 6px; }
  .person-lines { margin-top: 26px; font-size: 19px; line-height: 1.45; }
  .rule { height: 1px; background: var(--rule-gold); margin: 14px 0 12px; width: 640px; }
  .address { font-size: 19px; }
</style>
</head>
<body>
<main class="sheet">
  <section class="card card-front">
    <div class="brand">
      <span class="brand-dot"></span>
      <span class="brand-name">Relaymark Hub</span>
    </div>
  </section>

  <section class="card card-back">
    <svg class="corner-glow" width="360" height="470" viewBox="0 0 360 470" aria-hidden="true">
      <defs>
        <linearGradient id="cornerGrad" x1="0" y1="0" x2="1" y2="0.3">
          <stop offset="0" stop-color="#b9d47a"/>
          <stop offset="0.35" stop-color="#6fc79b"/>
          <stop offset="0.7" stop-color="#7fa0d2"/>
          <stop offset="1" stop-color="#c97a6e"/>
        </linearGradient>
      </defs>
      <path d="M120 0 H360 V420 C300 360 230 300 190 220 C150 140 130 70 120 0 Z" fill="url(#cornerGrad)"/>
    </svg>

    <div class="back-brand">
      <div class="brand">
        <span class="brand-dot"></span>
        <span class="brand-name">Relaymark Hub</span>
      </div>
      <p class="abn">ABN 41 902 615 273</p>
    </div>

    <div class="contact">
      <h1 class="person-name">Dale Pruitt</h1>
      <p class="person-role">Co-Founder | Managing Director</p>
      <p class="person-lines">+61 0491 528 307<br>dale.pruitt@corvelaxtro.com</p>
      <div class="rule"></div>
      <p class="address">Suite 718 263 Harrowgate Row Melbourne Vic 3000</p>
    </div>
  </section>
</main>
</body>
</html>
```